今までのデザインも今回からは撤廃して、新しいデザインで統一したいと思います。

ボディーソープ2種類、シャンプー2種類、コンディショナー2種類、ボディークリーム2種類(香りはどれも ブラックペッパー と ローズ)
ハンドソープ1種類 (シャンパンマスカットの香り)
ディッシュソープ1種類 (オレンジとグレープフルーツの香り)

文字だけを変えて、背景の色を変えるだけでもいいと思いますし、
香りが同じのものはデザイン一緒で文字だけ変えるでもいいかと思います。

天然由来成分98%以上で、ヴォルテリカで販売しており、
ボディーソープでも4800円とかなり高級なアイテムとなります。

シャンプー、コンディショナーも同じ価格です。
ボディークリームはもっと高価格帯になりますので、
ラベルに高級感が欲しいです。

オーガニックハーブと言えども、男性の購入者もかなり多いので、
ハーブだけど、カッコよく、家に置いてあるインテリアの一つとしても選ばれるような
斬新な遠くから見ても、すぐにTOVILの商品だと分かるようなデザインを希望します。

体臭を全て消して、異性からいいなと思われる香りが身体に残るプロダクトで作っており、
オーガニックハーブエキスで作った本当に品質にこだわって開発しました。

またディッシュソープは天然由来100%で手荒れをしない、寧ろ、手を労わる、治癒する効果として、手荒れが酷い女性にかなり好まれて使用頂いております。

なので、男性からも女性からも支持され、かつ高級感があり、シャープさとナチュラルさを兼ね備えた斬新なデザインをお願いしたいと思います。

かなり難しいお願いかとは思いますが何卒宜しくお願い致します。

tovil-example.co.jp
のサイトを見て頂いて、商品の特徴などは掴んで頂けたらと思います。

ただ、サイトイメージとしては、体臭ケアの効果がすごいのですが、
香水のようなボディーソープとして、かなり香りが残るのが特徴です。
しかも天然由来なので、美白、美肌効果も高く、男性の肘や膝のカサカサもなくなります。
今後サイトの作りもカッコよく作り直していく予定ですですので、
ボトルは変わらないので、イメージの参考にして頂けたらと思います。

現在のラベルサイズ 横215mm × 縦80mm

```html
<!DOCTYPE html>
<html lang="ja">
<head>
<meta charset="utf-8">
<title>TOVIL Organic Label Series</title>
<link href="https://fonts.googleapis.com/css2?family=Cormorant+Garamond:ital,wght@0,400;0,500;1,400&family=Noto+Sans+JP:wght@400;500&family=Yanone+Kaffeesatz:wght@300;400&display=swap" rel="stylesheet">
<style>
  :root {
    --paper: #ffffff;
    --ink: #4a4a4a;
    --rule: #d8d8d8;
    --pepper: #6b5560;
    --pepper-wave: #b3a8ae;
    --pepper-leaf: #6f8f3a;
    --rose: #ec8f8f;
    --rose-wave: #f3c7c2;
    --rose-flower: #e46a8c;
    --grape: #9cb42e;
    --grape-wave: #d3dc9c;
    --grape-fruit: #8fae3c;
    --citrus: #f08a2a;
    --citrus-wave: #f7bd8d;
    --citrus-fruit: #f2a93b;
  }
  * { margin: 0; padding: 0; box-sizing: border-box; }
  html, body { width: 846px; height: 1200px; overflow: hidden; background: var(--paper); }
  body { position: relative; font-family: "Noto Sans JP", sans-serif; color: var(--ink); }

  .variant { position: absolute; left: 92px; width: 662px; }
  .variant-head { display: flex; gap: 12px; align-items: flex-start; height: 44px; }
  .swatch { width: 20px; height: 20px; flex: none; margin-top: 2px; }
  .variant-head p { font-size: 10.5px; line-height: 17px; letter-spacing: 0.04em; }

  .label {
    position: relative; width: 640px; height: 238px; margin-left: 22px;
    background: var(--paper); border: 1px solid var(--rule); overflow: hidden;
  }
  .label .wave { position: absolute; inset: 0; width: 100%; height: 100%; }
  .brand {
    position: absolute; top: 16px; left: 0; right: 0; text-align: center;
    font-family: "Cormorant Garamond", serif; font-size: 15px; letter-spacing: 0.35em; color: #8a8a8a;
  }
  .art { position: absolute; left: 190px; top: 52px; width: 56px; height: 66px; border-radius: 40% 50% 45% 50%; }
  .organic {
    position: absolute; left: 246px; top: 60px;
    font-family: "Cormorant Garamond", serif; font-style: italic; font-size: 14px; color: #7a7a7a;
  }
  .product {
    position: absolute; left: 218px; top: 70px;
    font-family: "Yanone Kaffeesatz", sans-serif; font-weight: 300; font-size: 46px; letter-spacing: 0.02em; line-height: 1;
  }
  .tagline {
    position: absolute; left: 258px; top: 130px; width: 120px; text-align: center;
    font-family: "Cormorant Garamond", serif; font-size: 11px; line-height: 13px; color: #555;
  }
  .volume {
    position: absolute; bottom: 10px; left: 0; right: 0; text-align: center;
    font-family: "Cormorant Garamond", serif; font-size: 8px; color: #777;
  }

  .pepper { top: 20px; } .pepper .swatch { background: var(--pepper); } .pepper .product { color: var(--pepper); }
  .rose { top: 310px; } .rose .swatch { background: var(--rose); } .rose .product { color: var(--rose); }
  .grape { top: 600px; } .grape .swatch { background: var(--grape); } .grape .product { color: var(--grape); }
  .citrus { top: 890px; } .citrus .swatch { background: var(--citrus); } .citrus .product { color: var(--citrus); }
</style>
</head>
<body>

<section class="variant pepper">
  <header class="variant-head"><span class="swatch"></span><p>ブラックペッパー<br>ボディーソープ、シャンプー、コンディショナー、ボディークリーム</p></header>
  <div class="label">
    <svg class="wave" viewBox="0 0 640 238" preserveAspectRatio="none"><path d="M0 150 C150 150 220 200 330 150 C430 100 500 30 640 28 L640 238 L0 238 Z" fill="var(--pepper-wave)"/></svg>
    <div class="brand">TOVIL</div>
    <div class="art" role="img" aria-label="Black pepper leaves illustration" style="background:radial-gradient(circle at 40% 40%, #93b35a, var(--pepper-leaf))"></div>
    <div class="organic">Organic</div>
    <div class="product">Body soap</div>
    <p class="tagline">The fragrance of<br>black pepper</p>
    <div class="volume">500ml</div>
  </div>
</section>

<section class="variant rose">
  <header class="variant-head"><span class="swatch"></span><p>ローズ<br>ボディーソープ、シャンプー、コンディショナー、ボディークリーム</p></header>
  <div class="label">
    <svg class="wave" viewBox="0 0 640 238" preserveAspectRatio="none"><path d="M0 150 C150 150 220 200 330 150 C430 100 500 30 640 28 L640 238 L0 238 Z" fill="var(--rose-wave)"/></svg>
    <div class="brand">TOVIL</div>
    <div class="art" role="img" aria-label="Rose flower illustration" style="background:radial-gradient(circle at 45% 40%, #f4a6bd, var(--rose-flower))"></div>
    <div class="organic">Organic</div>
    <div class="product">Shampoo</div>
    <p class="tagline">The fragrance of rose</p>
    <div class="volume">500ml</div>
  </div>
</section>

<section class="variant grape">
  <header class="variant-head"><span class="swatch"></span><p>シャンパンマスカットの香り<br>ハンドソープ</p></header>
  <div class="label">
    <svg class="wave" viewBox="0 0 640 238" preserveAspectRatio="none"><path d="M0 150 C150 150 220 200 330 150 C430 100 500 30 640 28 L640 238 L0 238 Z" fill="var(--grape-wave)"/></svg>
    <div class="brand">TOVIL</div>
    <div class="art" role="img" aria-label="Champagne muscat grapes illustration" style="background:radial-gradient(circle at 45% 40%, #c5d97a, var(--grape-fruit))"></div>
    <div class="organic">Organic</div>
    <div class="product">Hand soap</div>
    <p class="tagline">The fragrance of<br>champagne Muscat</p>
    <div class="volume">500ml</div>
  </div>
</section>

<section class="variant citrus">
  <header class="variant-head"><span class="swatch"></span><p>オレンジとグレープフルーツの香り<br>ディッシュソープ</p></header>
  <div class="label">
    <svg class="wave" viewBox="0 0 640 238" preserveAspectRatio="none"><path d="M0 150 C150 150 220 200 330 150 C430 100 500 30 640 28 L640 238 L0 238 Z" fill="var(--citrus-wave)"/></svg>
    <div class="brand">TOVIL</div>
    <div class="art" role="img" aria-label="Orange and grapefruit slices illustration" style="background:radial-gradient(circle at 45% 40%, #f9d27a, var(--citrus-fruit))"></div>
    <div class="organic">Organic</div>
    <div class="product">Dish soap</div>
    <p class="tagline">The fragrance of<br>the orange and the grapefruit</p>
    <div class="volume">500ml</div>
  </div>
</section>

</body>
</html>
```